Content processing platform needs a landing page for products

We need a general landing page for products that we are launching. The concept of the product page is to do two things: a) Get users to sign up for our waitlist (que) so they get access to the product (we give access weekly). b) To generate interest for future products that we have not decided on yet. Mockups: Please see our mockups for inspiration. You have pretty free hands to combine, but please don't let our users think :-). Style: Please use the colours of our style sheet and see the home page (penlyhub.com) for inspiration on how we want the style and tone to be. The final design should communicate "scaling".

Target Market(s)

B2B - online businesses big and small that wish to scale their production of content and translation.

Industry/Entity Type

SaaS

Number of Pages Required

1 page

Font styles to use
Other font styles liked:
• open sans

Requirements
Must have
• Follow our styleguide.

```html
<!DOCTYPE html>
<html lang="en">
<head>
<meta charset="utf-8">
<title>Penlyhub – Content Processing Platform</title>
<link rel="stylesheet" href="https://fonts.googleapis.com/css2?family=Open+Sans:wght@300;400;600;700;800&display=swap">
<style>
:root{
  --blue:#1ea7e1;
  --blue-dark:#0d7fc0;
  --green:#63e6a4;
  --teal:#27c0b4;
  --pink:#f0386b;
  --ink:#333a40;
  --text:#5b6168;
  --muted:#8b9096;
  --line:#dde1e5;
  --soft:#f3f4f6;
  --band:#eceef1;
  --footer:#333333;
  --navy:#13354d;
  --white:#ffffff;
  --star:#f5b820;
}
*{box-sizing:border-box;margin:0;padding:0}
html,body{width:1200px;height:5357px;overflow:hidden}
body{font-family:"Open Sans",Arial,sans-serif;color:var(--text);background:var(--white);position:relative}
section,header,footer{position:relative;width:1200px;overflow:hidden}
a{color:inherit;text-decoration:none}

/* Hero */
.hero{height:770px;background:linear-gradient(160deg,#1fb4e6 0%,#1ba6d8 30%,#22c0b8 70%,#34d0a6 100%)}
.hero-wave{position:absolute;left:0;bottom:0;width:1200px;height:150px}
.nav{position:absolute;top:36px;left:100px;right:93px;height:40px;display:flex;align-items:center}
.brand{font-size:30px;font-weight:700;color:var(--white);letter-spacing:-.5px}
.nav-links{display:flex;gap:34px;margin-left:257px;font-size:16px;font-weight:600;color:var(--white);letter-spacing:.3px}
.nav-cta{margin-left:auto;border:2px solid var(--white);color:var(--white);font-size:13px;font-weight:600;padding:10px 22px;letter-spacing:.3px}
.hero-title{position:absolute;left:100px;top:232px;width:440px;font-size:32px;line-height:54px;font-weight:800;color:var(--white);text-transform:uppercase;letter-spacing:-.2px;white-space:nowrap;z-index:1}
.hero-title .accent{color:var(--green)}
.btn-pink{display:inline-block;background:var(--pink);color:var(--white);font-weight:600;font-size:20px;padding:14px 40px}
.hero .btn-pink{position:absolute;left:100px;top:503px;padding:14px 42px}
.hero-screen{position:absolute;left:607px;top:243px;width:463px;height:382px;border-radius:14px;background:linear-gradient(160deg,#e9eef2,#c7d1d8);box-shadow:0 10px 30px rgba(0,0,0,.18)}

/* Trust bar */
.trust{height:100px;display:flex;align-items:center;padding:0 100px}
.trust-lead{display:flex;align-items:center;gap:18px}
.trust-lead strong{display:block;font-size:28px;color:var(--ink);font-weight:700;line-height:32px}
.trust-lead span{font-size:16px;color:var(--text)}
.stats{display:flex;margin-left:auto;gap:66px;text-align:center}
.stat b{display:block;font-size:36px;font-weight:600;color:var(--blue);line-height:40px}
.stat span{font-size:16px;color:var(--text)}

/* Features */
.features{height:523px;text-align:center}
.section-title{font-size:42px;font-weight:400;color:var(--ink)}
.section-sub{font-size:20px;color:var(--text)}
.features .section-title{padding-top:40px}
.features .section-sub{margin-top:16px}
.feature-row{display:flex;gap:33px;justify-content:center;margin-top:60px}
.feature{width:250px;height:186px;background:var(--soft);border-bottom:4px solid var(--line);display:flex;flex-direction:column;align-items:center;justify-content:center;gap:26px;font-size:17px;color:var(--ink)}
.feature svg{width:60px;height:60px}

/* Steps */
.steps{height:767px;background:linear-gradient(115deg,#1572b8 0%,#2a5ea8 35%,#6a4c8f 65%,#c9415e 100%);text-align:center;color:var(--white)}
.steps .section-title{color:var(--white);font-weight:300;padding-top:92px;line-height:58px;font-size:44px}
.steps .section-sub{color:var(--white);margin-top:26px}
.step-row{position:absolute;top:364px;left:100px;width:1007px;height:268px}
.step{position:absolute;top:0;width:300px;height:268px;background:var(--white);box-shadow:0 8px 24px rgba(0,0,0,.18)}
.step-num{position:absolute;top:-32px;left:118px;width:64px;height:64px;border-radius:50%;background:var(--pink);border:5px solid var(--white);box-shadow:0 3px 10px rgba(0,0,0,.2);color:var(--white);font-size:26px;font-weight:600;line-height:54px}
.step h3{margin-top:80px;font-size:20px;font-weight:600;color:var(--pink)}
.step p{margin:24px 34px 0;font-size:17px;line-height:26px;color:var(--text)}
.step-arrow{position:absolute;top:110px;width:30px;height:50px}
.steps-wave{position:absolute;left:0;bottom:0;width:1200px;height:140px}

/* Plans */
.plans{height:715px;text-align:center}
.plans .section-title{padding-top:72px}
.plans .section-sub{margin-top:14px}
.plan-table{position:absolute;left:100px;top:247px;width:1000px;border-collapse:collapse;font-size:11px;color:var(--text);box-shadow:0 2px 10px rgba(0,0,0,.08)}
.plan-table th{height:54px;background:#5a5d60;color:var(--white);font-size:17px;font-weight:400;text-transform:uppercase;border-right:1px solid #777}
.plan-table th.featured{background:var(--pink)}
.plan-table td{height:38px;border-bottom:1px solid var(--line);text-align:center;background:var(--white)}
.plan-table td:first-child{color:var(--ink)}
.plan-table tr.price td{color:var(--blue);font-weight:600}
.plan-actions{position:absolute;left:346px;top:587px;width:754px;display:flex}
.plan-actions span{flex:1;display:flex;justify-content:center}
.btn-plan{background:#5a5d60;color:var(--white);font-size:11px;font-weight:600;padding:10px 16px;text-transform:uppercase}
.btn-plan.featured{background:var(--pink)}

/* Reviews */
.reviews{height:689px;background:var(--band);text-align:center}
.reviews .section-title{padding-top:90px}
.review-row{position:absolute;top:218px;left:100px;width:1007px}
.review{position:absolute;top:0;width:300px;height:325px;background:var(--white);border:2px solid #d3d7db;text-align:left;padding:40px 26px}
.review .stars{position:absolute;top:18px;right:26px;color:var(--star);font-size:14px;letter-spacing:1px}
.review h4{font-size:20px;font-weight:400;color:var(--blue)}
.review p{margin-top:28px;font-size:16px;line-height:25px;color:var(--text)}
.review .quote{position:absolute;right:26px;bottom:-6px;font-size:110px;line-height:110px;color:#d6d9dd;font-family:Georgia,serif}
.dots{position:absolute;top:632px;left:0;width:1200px;display:flex;justify-content:center;gap:14px}
.dots i{width:22px;height:22px;border-radius:50%;border:2px solid var(--blue)}
.dots i.on{background:var(--blue)}

/* FAQ */
.faq{height:836px}
.faq .section-title{position:absolute;left:428px;top:100px;width:400px;font-size:44px}
.faq-art{position:absolute;left:64px;top:186px;width:330px;height:428px;border-radius:50% 50% 40% 40%;background:radial-gradient(circle at 50% 40%,#f1f4f7,#dde6ee)}
.faq-list{position:absolute;left:428px;top:221px;width:672px}
.faq-item{border:2px solid var(--line);display:flex;align-items:center;justify-content:space-between;padding:0 24px;height:102px;margin-bottom:28px;font-size:30px;color:var(--ink)}
.faq-item.open{display:block;background:#eaf5fb;border-color:#cde6f4;height:215px;padding:20px 24px;margin-bottom:0}
.faq-item.open .q{display:flex;justify-content:space-between;align-items:center;font-size:28px;color:var(--blue);padding-bottom:6px;border-bottom:2px solid var(--white)}
.faq-item.open p{margin-top:14px;font-size:20px;line-height:32px;color:var(--ink)}
.sign{font-size:40px;font-weight:300;color:var(--ink);line-height:40px}

/* Clients */
.clients{height:386px;text-align:center}
.clients .section-title{padding-top:36px;font-size:42px}
.client-row{display:flex;justify-content:center;gap:96px;margin-top:60px;align-items:center}
.client{display:flex;align-items:center;gap:10px;font-size:34px;font-weight:600;color:#8a8f95}
.client i{width:22px;height:22px;background:#8a8f95}

/* CTA */
.cta{position:absolute;left:296px;top:4685px;width:600px;height:215px;background:var(--blue);text-align:center;color:var(--white);z-index:2}
.cta h2{margin-top:36px;font-size:40px;font-weight:400}
.cta p{margin-top:4px;font-size:17px}
.btn-dark{display:inline-block;margin-top:26px;background:#2a2f33;color:var(--white);font-size:15px;font-weight:600;padding:10px 40px}

/* Footer */
.footer{height:464px;background:var(--footer);color:#e6e6e6}
.footer-cols{position:absolute;top:214px;left:118px;width:1000px;display:flex}
.footer-col{font-size:17px;line-height:30px}
.footer-col:nth-child(1){width:364px}
.footer-col:nth-child(2){width:411px}
.footer-col .current{color:var(--blue);text-decoration:underline}
.legal{height:107px;background:var(--navy);display:flex;align-items:center;padding:0 100px 0 107px}
.social{display:flex;gap:14px}
.social i{width:34px;height:34px;background:var(--blue)}
.social i:nth-child(3){background:#1e88c8}
.social i:nth-child(4){background:var(--pink)}
.social i:nth-child(5){background:#e0413b}
.legal p{margin-left:auto;color:#e6e6e6;font-size:16px}
</style>
</head>
<body>

<header class="hero">
  <nav class="nav">
    <a class="brand" href="#">Penlyhub</a>
    <div class="nav-links"><a href="#">PRODUCTS</a><a href="#">APPS</a><a href="#">PRICES</a><a href="#">BLOG</a><a href="#">HELP</a></div>
    <a class="nav-cta" href="#">SCALE YOUR BUSINESS</a>
  </nav>
  <h1 class="hero-title">Manage your<br><span class="accent">content</span> with our new<br>content <span class="accent">processing</span><br><span class="accent">platform</span></h1>
  <a class="btn-pink" href="#">Learn More</a>
  <div class="hero-screen" role="img" aria-label="Laptop showing a product video of the content platform"></div>
  <svg class="hero-wave" viewBox="0 0 1200 150" preserveAspectRatio="none" aria-hidden="true">
    <path d="M0 70 C200 20 380 110 600 80 C820 50 980 10 1200 60 L1200 150 L0 150Z" fill="#ffffff" opacity=".35"/>
    <path d="M0 110 C240 60 420 140 640 112 C860 84 1000 70 1200 100 L1200 150 L0 150Z" fill="#ffffff"/>
  </svg>
</header>

<section class="trust">
  <div class="trust-lead">
    <svg width="60" height="60" viewBox="0 0 60 60" aria-hidden="true" fill="none" stroke="#5b6168" stroke-width="2"><path d="M18 8h24v16a12 12 0 0 1-24 0z"/><path d="M18 13H8a10 10 0 0 0 10 12M42 13h10a10 10 0 0 1-10 12"/><path d="M30 36v10M20 52h20v-6H20z"/></svg>
    <div><strong>Trusted by 4000+</strong><span>High performing team worldwide</span></div>
  </div>
  <div class="stats">
    <div class="stat"><b>0035984</b><span>Downloads</span></div>
    <div class="stat"><b>00359+</b><span>Active Installs</span></div>
    <div class="stat"><b>0035984</b><span>Paid Users</span></div>
  </div>
</section>

<section class="features">
  <h2 class="section-title">Continuous improvement of your Business</h2>
  <p class="section-sub">Get a weekly access now and enjoy features of</p>
  <div class="feature-row">
    <div class="feature"><svg viewBox="0 0 60 60" fill="none" stroke="#f0386b" stroke-width="2"><rect x="8" y="12" width="44" height="30" rx="2"/><path d="M22 50h16M30 42v8M20 27l7 6 13-12"/></svg>Weekly Access</div>
    <div class="feature"><svg viewBox="0 0 60 60" fill="none" stroke="#f0386b" stroke-width="2"><path d="M30 10 52 48H8z"/><path d="M30 24v12M30 41v2"/><circle cx="30" cy="32" r="26" stroke="#5b6168" stroke-dasharray="4 5"/></svg>Risk Free</div>
    <div class="feature"><svg viewBox="0 0 60 60" fill="none" stroke="#f0386b" stroke-width="2"><rect x="8" y="12" width="44" height="36" rx="2"/><path d="M8 20h44"/><circle cx="30" cy="34" r="7"/><path d="M30 24v3M30 41v3M20 34h3M37 34h3"/></svg>Automatic</div>
    <div class="feature"><svg viewBox="0 0 60 60" fill="none" stroke="#f0386b" stroke-width="2"><circle cx="30" cy="30" r="16"/><path d="M14 30h32M30 14c-8 9-8 23 0 32M30 14c8 9 8 23 0 32"/><path d="M30 4v6M30 50v6M4 30h6M50 30h6" stroke="#5b6168"/></svg>Seamless</div>
  </div>
</section>

<section class="steps">
  <h2 class="section-title">Three Steps to have continus improvement<br>of your [New Product]</h2>
  <p class="section-sub">If you are struggling with the problems then let us know.</p>
  <div class="step-row">
    <div class="step" style="left:0"><div class="step-num">1</div><h3>Step One Title</h3><p>Lorem ipsum dolor sit amet, consectetur and adipiscing elit, sed do eiusmod tempor.</p></div>
    <svg class="step-arrow" style="left:300px" viewBox="0 0 30 50" aria-hidden="true"><path d="M0 0h8l18 25-18 25H0z" fill="#fff"/><path d="M6 16l9 9-9 9" fill="none" stroke="#5a5d60" stroke-width="3"/></svg>
    <div class="step" style="left:353px"><div class="step-num">2</div><h3>Step Two Title</h3><p>Lorem ipsum dolor sit amet, consectetur and adipiscing elit, sed do eiusmod tempor.</p></div>
    <svg class="step-arrow" style="left:653px" viewBox="0 0 30 50" aria-hidden="true"><path d="M0 0h8l18 25-18 25H0z" fill="#fff"/><path d="M6 16l9 9-9 9" fill="none" stroke="#5a5d60" stroke-width="3"/></svg>
    <div class="step" style="left:707px"><div class="step-num">3</div><h3>Step Three Title</h3><p>Lorem ipsum dolor sit amet, consectetur and adipiscing elit, sed do eiusmod tempor.</p></div>
  </div>
  <svg class="steps-wave" viewBox="0 0 1200 140" preserveAspectRatio="none" aria-hidden="true">
    <path d="M0 60 C220 20 380 120 620 80 C860 40 1000 30 1200 70 L1200 140 L0 140Z" fill="#ffffff" opacity=".35"/>
    <path d="M0 100 C240 50 420 130 660 100 C880 72 1020 80 1200 110 L1200 140 L0 140Z" fill="#ffffff"/>
  </svg>
</section>

<section class="plans">
  <h2 class="section-title">Explore more features by selecting a plan</h2>
  <p class="section-sub">Choose the best solution for your business.</p>
  <table class="plan-table">
    <colgroup><col style="width:246px"><col style="width:172px"><col style="width:193px"><col style="width:193px"><col style="width:196px"></colgroup>
    <tr><th>Plan Title</th><th>Local</th><th class="featured">National</th><th>Multinational</th><th>Global</th></tr>
    <tr><td>Language Limit</td><td>1 Language</td><td>2 Language</td><td>4 Language</td><td>Unlimited Language</td></tr>
    <tr><td>Copywriters</td><td>5 Different Writers</td><td>10 Different Writers</td><td>40 Different Writers</td><td>100 Different Writers</td></tr>
    <tr><td>Jobs</td><td>5 Jobs</td><td>5 Jobs</td><td>30 Jobs</td><td>100 Jobs</td></tr>
    <tr><td>Ad Copy Variations</td><td>4 to 5</td><td>44 to 75</td><td>136</td><td>722</td></tr>
    <tr><td>Guaranteed Winning<br>Experiments (each month)</td><td>1 to 3</td><td>4 to 5</td><td>15 to 16</td><td>40 to 150</td></tr>
    <tr class="price"><td>Price/month</td><td>€45</td><td>€167</td><td>€331</td><td>€993</td></tr>
  </table>
  <div class="plan-actions">
    <span><a class="btn-plan" href="#">Get on the list</a></span>
    <span><a class="btn-plan featured" href="#">Get on the list</a></span>
    <span><a class="btn-plan" href="#">Get on the list</a></span>
    <span><a class="btn-plan" href="#">Get on the list</a></span>
  </div>
</section>

<section class="reviews">
  <h2 class="section-title">Client Reviews</h2>
  <div class="review-row">
    <article class="review" style="left:0"><span class="stars">★★★★★</span><h4>Client Name</h4><p>Lorem ipsum dolor sit amet, consectetur and adipiscing elit, sed do eiusmod tempor. Ipsum dolor sit amet, consectetur and adipiscing eit.</p><span class="quote">“</span></article>
    <article class="review" style="left:353px"><span class="stars">★★★★★</span><h4>Client Name</h4><p>Lorem ipsum dolor sit amet, consectetur and adipiscing elit, sed do eiusmod tempor. Ipsum dolor sit amet, consectetur and adipiscing eit.</p><span class="quote">“</span></article>
    <article class="review" style="left:707px"><span class="stars">★★★★★</span><h4>Client Name</h4><p>Lorem ipsum dolor sit amet, consectetur and adipiscing elit, sed do eiusmod tempor. Ipsum dolor sit amet, consectetur and adipiscing eit.</p><span class="quote">“</span></article>
  </div>
  <div class="dots"><i></i><i class="on"></i><i></i></div>
</section>

<section class="faq">
  <h2 class="section-title">Have a Question?</h2>
  <div class="faq-art" role="img" aria-label="Line illustration of a support agent wearing a headset"></div>
  <div class="faq-list">
    <div class="faq-item open">
      <div class="q">What is Lorem Ipsum?<span class="sign">—</span></div>
      <p>Lorem Ipsum is simply dummy text of the printing and typesetting industry. Lorem Ipsum has been the industry's.</p>
    </div>
    <div style="height:28px"></div>
    <div class="faq-item">Lorem Ipsum is simply dummy text?<span class="sign">+</span></div>
    <div class="faq-item">Lorem Ipsum has been the industry?<span class="sign">+</span></div>
  </div>
</section>

<section class="clients">
  <h2 class="section-title">Trusted by over 10000 clients</h2>
  <div class="client-row">
    <span class="client"><i></i>Chatloop</span>
    <span class="client">Findora</span>
    <span class="client">Shopmere</span>
    <span class="client">Paywell</span>
    <span class="client"><i></i>Cartsy</span>
  </div>
</section>

<div class="cta">
  <h2>We build it. You rock it.</h2>
  <p>A complete and customizable solution to your dreams.</p>
  <a class="btn-dark" href="#">Register Now</a>
</div>

<footer class="footer">
  <div class="footer-cols">
    <div class="footer-col">
      <a class="current" href="#">- About Us</a><br>- Team<br>- Contact<br>- Terms of Service<br>- Privacy Policy<br>- Imprint
    </div>
    <div class="footer-col">
      - Penlyhub Affiliate<br>- Careers<br>- Developer Resources<br>- Penlyhub Workshops<br>- Help
    </div>
    <div class="footer-col">
      Penlyhub B.V.<br>Harbour Lane 114 2011 KD<br>Haarlem The Netherlands<br>Tel: +31 (0)10 555 0142<br>VAT: NL000000000B01
    </div>
  </div>
</footer>
<div class="legal">
  <div class="social" aria-label="Social links"><i></i><i></i><i></i><i></i><i></i></div>
  <p>© 2018 Penlyhub. All Rights Reserved.</p>
</div>

</body>
</html>
```